web page template design

We'd like to see a few designs based on the selected logo. See attached color logo.

We'll need a homepage design which will display the competition announcement and limited details about it. There will be links (or tabs) to the follow on pages which will contain all of the legal details, sign-up and design submission page, finalist selection page, winner announcement page, jury (judges) background page, company sponsor (Verant) details, press release page and a blog page. These are just guidelines for the number of subpage links.

So we'd like a primary page and a follow-on page which is a little more plain.

Here is the competition briefer below:

In January 2014, Verant Tile Inc. will launch its 1st Annual Verant Tile Floor Design Competition. This design competition will be open to Design and Architecture students of the NYC area. Students and student groups can submit cork flooring design concepts online to a judging committee of prominent designers and architects who will select design finalists and a winner. The winning design will highlight the unique creative possibilities of sustainable cork tiles. The winner will receive a cash prize and publication of their winning design through press releases and various media outlets as well as on the PlankMosaic.example website. The winning floor will be created and photographed by Verant Tile and will be donated to a deserving non-profit community center in NYC. The donated cork floor will be installed at no cost to the non-profit community center.

Target Market(s)

designers and architects.

Industry/Entity Type

Non-Profit

Requirements
Must have
• tabs or link system

```html
<!DOCTYPE html>
<html lang="en">
<head>
<meta charset="utf-8">
<title>Judges – Verant Tile Floor Design Competition</title>
<link href="https://fonts.googleapis.com/css2?family=Roboto+Condensed:ital,wght@0,400;0,700;1,400&display=swap" rel="stylesheet">
<style>
  :root {
    --ink-black: #141414;
    --page-grey: #dcddd8;
    --paper: #f6f6f5;
    --brand-red: #b83f3a;
    --fold-dark: #1c1c1c;
    --nav-text: #e8e8e8;
    --nav-active: #d4cf6e;
    --heading-text: #333333;
    --body-text: #9a9a9a;
    --rule: #d6d6d3;
    --thumb-fill: #dcddd8;
    --thumb-line: #a8a9a4;
    --footer-text: #d0d0d0;
  }
  * { margin: 0; padding: 0; box-sizing: border-box; }
  html, body { width: 1200px; height: 1000px; overflow: hidden; }
  body {
    position: relative;
    background: var(--page-grey);
    font-family: "Roboto Condensed", "Arial Narrow", sans-serif;
  }
  .site-header {
    position: absolute; left: 0; top: 0; width: 1200px; height: 163px;
    background: repeating-linear-gradient(135deg, #181818 0 2px, #101010 2px 4px);
    box-shadow: 0 2px 4px rgba(0,0,0,.25);
    z-index: 2;
  }
  .brand {
    position: absolute; left: 62px; top: 52px;
    display: flex; align-items: center; gap: 14px;
  }
  .brand-dot {
    flex: none; width: 44px; height: 44px;
    border: 3px solid #ffffff; border-radius: 50%;
  }
  .brand-name {
    width: 160px;
    color: #ffffff; font-size: 17px; font-weight: 700; line-height: 21px;
  }
  .main-nav a {
    position: absolute; top: 38px;
    color: var(--nav-text); text-decoration: none;
    font-size: 15.5px; font-weight: 700;
  }
  .main-nav a.is-current { color: var(--nav-active); }
  .signup-tab {
    position: absolute; left: 1090px; top: 0; width: 39px; height: 141px;
    text-decoration: none;
  }
  .signup-tab svg { position: absolute; inset: 0; }
  .signup-label {
    position: absolute; left: 50%; top: 58px;
    transform: translate(-50%, -50%) rotate(-90deg);
    color: #ffffff; font-weight: 700; font-size: 17px; letter-spacing: .5px; white-space: nowrap;
  }
  .content-panel {
    position: absolute; left: 38px; top: 163px; width: 1124px; height: 782px;
    background: var(--paper);
  }
  .page-ribbon { position: absolute; left: 8px; top: 211px; width: 430px; height: 123px; z-index: 1; }
  .page-ribbon svg { position: absolute; inset: 0; }
  .page-title {
    position: absolute; left: 141px; top: 24px;
    color: #ffffff; font-size: 34px; font-weight: 700; letter-spacing: .3px;
  }
  .column-rule {
    position: absolute; left: 457px; top: 272px; width: 1px; height: 631px;
    background: var(--rule);
  }
  .judge { position: absolute; width: 640px; }
  .judge-photo { position: absolute; left: 0; top: 0; width: 107px; height: 107px; }
  .judge-text { position: absolute; left: 125px; top: 0; width: 515px; }
  .judge-name {
    font-size: 19.5px; font-weight: 700; color: var(--heading-text); letter-spacing: 1px;
  }
  .judge-role {
    font-size: 17px; font-weight: 400; font-style: italic; color: var(--heading-text);
    margin-left: 12px;
  }
  .judge-role::before { content: "|"; font-style: normal; font-weight: 700; margin-right: 7px; }
  .judge-bio {
    margin-top: 20px; font-size: 15.5px; line-height: 20px; color: var(--body-text);
    white-space: nowrap; letter-spacing: .35px;
  }
  .site-footer {
    position: absolute; left: 0; top: 945px; width: 1200px; height: 55px;
    background: repeating-linear-gradient(135deg, #181818 0 2px, #101010 2px 4px);
    box-shadow: 0 -2px 4px rgba(0,0,0,.2);
    color: var(--footer-text); font-size: 11px; font-weight: 700;
    text-align: center; line-height: 66px;
  }
</style>
</head>
<body>
  <header class="site-header">
    <div class="brand">
      <span class="brand-dot"></span>
      <span class="brand-name">Verant Tile Floor Design Competition</span>
    </div>
    <nav class="main-nav">
      <a href="#" style="left:399px">About Verant</a>
      <a href="#" class="is-current" style="left:530px">Judges</a>
      <a href="#" style="left:617px">Legal</a>
      <a href="#" style="left:691px">Finalists</a>
      <a href="#" style="left:788px">Winner!</a>
      <a href="#" style="left:878px">Press Releases</a>
      <a href="#" style="left:1020px">Blog</a>
    </nav>
    <a href="#" class="signup-tab">
      <svg width="39" height="141" viewBox="0 0 39 141"><polygon points="0,0 39,0 39,109 19.5,141 0,109" fill="var(--brand-red)"/></svg>
      <span class="signup-label">SIGN-UP</span>
    </a>
  </header>

  <main class="content-panel"></main>

  <div class="page-ribbon">
    <svg width="430" height="123" viewBox="0 0 430 123">
      <polygon points="0,85 28,85 28,122" fill="var(--fold-dark)"/>
      <polygon points="0,0 357,0 428,42 357,85 0,85" fill="var(--brand-red)"/>
    </svg>
    <h1 class="page-title">Judges</h1>
  </div>

  <div class="column-rule"></div>

  <article class="judge" style="left:495px; top:362px;">
    <svg class="judge-photo" role="img" aria-label="Judge portrait" viewBox="0 0 107 107">
      <rect x="0.5" y="0.5" width="106" height="106" fill="var(--thumb-fill)" stroke="var(--thumb-line)"/>
      <line x1="0" y1="0" x2="107" y2="107" stroke="var(--thumb-line)"/>
      <line x1="107" y1="0" x2="0" y2="107" stroke="var(--thumb-line)"/>
    </svg>
    <div class="judge-text">
      <h2><span class="judge-name">JOHN DOE</span><span class="judge-role">Architect at Halvorsen University</span></h2>
      <p class="judge-bio">Lorem ipsum dolor sit amet, consectetur adipisicing elit, sed do eiusmod<br>tempor incididunt ut labore et dolore magna aliqua. Ut enim ad minim<br>veniam, quis nostrud exercitation ullamco laboris nisi ut aliquip ex.</p>
    </div>
  </article>

  <article class="judge" style="left:498px; top:554px;">
    <svg class="judge-photo" role="img" aria-label="Judge portrait" viewBox="0 0 107 107">
      <rect x="0.5" y="0.5" width="106" height="106" fill="var(--thumb-fill)" stroke="var(--thumb-line)"/>
      <line x1="0" y1="0" x2="107" y2="107" stroke="var(--thumb-line)"/>
      <line x1="107" y1="0" x2="0" y2="107" stroke="var(--thumb-line)"/>
    </svg>
    <div class="judge-text">
      <h2><span class="judge-name">JOHN DOE</span><span class="judge-role">Architect at Halvorsen University</span></h2>
      <p class="judge-bio">Lorem ipsum dolor sit amet, consectetur adipisicing elit, sed do eiusmod<br>tempor incididunt ut labore et dolore magna aliqua. Ut enim ad minim<br>veniam, quis nostrud exercitation ullamco laboris nisi ut aliquip ex.</p>
    </div>
  </article>

  <article class="judge" style="left:498px; top:754px;">
    <svg class="judge-photo" role="img" aria-label="Judge portrait" viewBox="0 0 107 107">
      <rect x="0.5" y="0.5" width="106" height="106" fill="var(--thumb-fill)" stroke="var(--thumb-line)"/>
      <line x1="0" y1="0" x2="107" y2="107" stroke="var(--thumb-line)"/>
      <line x1="107" y1="0" x2="0" y2="107" stroke="var(--thumb-line)"/>
    </svg>
    <div class="judge-text">
      <h2><span class="judge-name">JOHN DOE</span><span class="judge-role">Architect at Halvorsen University</span></h2>
      <p class="judge-bio">Lorem ipsum dolor sit amet, consectetur adipisicing elit, sed do eiusmod<br>tempor incididunt ut labore et dolore magna aliqua. Ut enim ad minim<br>veniam, quis nostrud exercitation ullamco laboris nisi ut aliquip ex.</p>
    </div>
  </article>

  <footer class="site-footer">Copyright © 2013 Verant Tile Floor Design Competition</footer>
</body>
</html>
```